Brantley Studios photography and video creator

I need a business card for my production company. I shoot photography and videography for real estate, adventure sports and businesses

Contact Information for Business Card

simple not to busy

Colors

Designer to choose colors to be used in the design.

Requirements
Must have
• derek@brantleystudios.ca
• phone -5873304127
• instagram derek_brantley

```html
<!DOCTYPE html>
<html lang="en">
<head>
<meta charset="utf-8">
<title>Brantley Studios — Business Card</title>
<link href="https://fonts.googleapis.com/css2?family=Lato:wght@400;700;900&family=Montserrat:wght@700&display=swap" rel="stylesheet">
<style>
  :root {
    --stage: #d9d9db;
    --card-dark: #1b1a1f;
    --card-light: #ffffff;
    --ink: #111111;
    --ink-soft: #222222;
    --mark-fill: #2a2a2e;
    --mark-ring: #7a7a7e;
    --on-dark: #ffffff;
  }
  * { margin: 0; padding: 0; box-sizing: border-box; }
  html, body { width: 1200px; height: 1200px; overflow: hidden; }
  body {
    background: var(--stage);
    font-family: "Lato", sans-serif;
    position: relative;
  }
  .card {
    position: absolute;
    width: 600px;
    height: 343px;
    box-shadow: 0 12px 30px rgba(0,0,0,0.18);
  }
  .card--back {
    left: 300px;
    top: 150px;
    background: var(--card-dark);
    border-radius: 70px 0 70px 0;
    display: flex;
    align-items: center;
    justify-content: center;
  }
  .card--front {
    left: 300px;
    top: 600px;
    background: var(--card-light);
    border-radius: 0 70px 0 70px;
  }
  .brand {
    display: flex;
    align-items: center;
    gap: 14px;
  }
  .brand__dot {
    width: 54px;
    height: 54px;
    border-radius: 50%;
    background: var(--mark-fill);
    border: 3px solid var(--mark-ring);
  }
  .brand__name {
    font-family: "Lato", sans-serif;
    font-weight: 900;
    font-size: 28px;
    letter-spacing: 1px;
    text-transform: uppercase;
  }
  .card--back .brand__name { color: var(--on-dark); }
  .card--back .brand__dot { background: #3a3a3f; }
  .card--front .brand {
    position: absolute;
    right: 40px;
    top: 96px;
  }
  .card--front .brand__name { color: var(--ink); font-size: 24px; }
  .holder-name {
    position: absolute;
    left: 40px;
    top: 44px;
    font-family: "Montserrat", sans-serif;
    font-weight: 700;
    font-size: 19px;
    color: var(--ink);
    letter-spacing: 0.3px;
  }
  .contact-list {
    position: absolute;
    left: 40px;
    bottom: 52px;
    list-style: none;
    font-size: 16px;
    color: var(--ink-soft);
    line-height: 1.45;
  }
  .contact-list li { display: flex; align-items: center; gap: 8px; }
  .contact-list svg { width: 13px; height: 13px; fill: var(--ink); flex: none; }
  .social-handle {
    position: absolute;
    right: 40px;
    bottom: 30px;
    font-size: 16px;
    color: var(--ink-soft);
  }
</style>
</head>
<body>
  <section class="card card--back" aria-label="Card back">
    <div class="brand">
      <span class="brand__dot"></span>
      <span class="brand__name">Brantley Studios</span>
    </div>
  </section>

  <section class="card card--front" aria-label="Card front">
    <h1 class="holder-name">DEREK BRANTLEY</h1>

    <div class="brand">
      <span class="brand__dot"></span>
      <span class="brand__name">Brantley Studios</span>
    </div>

    <ul class="contact-list">
      <li>
        <svg viewBox="0 0 16 16" aria-hidden="true"><path d="M3 1h3l1.5 4-2 1.3a9 9 0 0 0 4.2 4.2L11 8.5l4 1.5v3a2 2 0 0 1-2 2A13 13 0 0 1 1 3a2 2 0 0 1 2-2z"/></svg>
        5873304127
      </li>
      <li>
        <svg viewBox="0 0 16 16" aria-hidden="true"><path d="M1 3h14v10H1z M1 3l7 5 7-5" fill="none" stroke="#111" stroke-width="1.8"/></svg>
        derek@brantleystudios.ca
      </li>
      <li>
        <svg viewBox="0 0 16 16" aria-hidden="true"><circle cx="8" cy="8" r="7"/><path d="M1 8h14M8 1c3 3 3 11 0 14M8 1c-3 3-3 11 0 14" fill="none" stroke="#fff" stroke-width="1"/></svg>
        www.brantleystudios.ca
      </li>
    </ul>

    <div class="social-handle">derek_brantley</div>
  </section>
</body>
</html>
```